KV Group

We need a new website for our company and since we had a very good work done for our logo in this site, we're back for the entire job.

Our company name is Marlowe Capital Group. We're adding files of examples of what we have done today. In my opinion we need a more attention lock in the site but yet financial simple work.

Our files (attached) will let you know what we have so far. We need a complete change but the colours should be the same, however you can change them not running away to far from the original, and of course matching with the logo.

We need examples for 3 kind of layouts.

- A HOME welcome layout
- An internal Layout with sidebar
- And internal Layout wide

We can buy image licenses if needed for assets.
Actually there are 5 slide images placed on the Welcome HOME, we need those there, but you can improve with better images to match the new website!!!

Target Market(s)

Clients looking for financial advisers, tax and funds specialist, currency advisers

Industry/Entity Type

Financial

Requirements
Must have
• all the fonts must be in accordance with the financial market sites........the welcome home page must be precise, neat and information accurate........the menu should be elegant........main focus on the Home page, should be also the PRIVATE ACCESS box log in.......

```html
<!DOCTYPE html>
<html lang="en">
<head>
<meta charset="utf-8">
<title>Marlowe Capital Group</title>
<link href="https://fonts.googleapis.com/css2?family=Arimo:wght@400;700&display=swap" rel="stylesheet">
<style>
:root{
  --orange:#f47a20;
  --orange-dark:#e0661a;
  --brown:#4a2810;
  --brown-dark:#2c1606;
  --text:#666;
  --grey-bg:#e6e6e6;
  --footer:#3b3b3b;
  --footer-2:#2f2f2f;
  --footer-3:#1c1c1c;
  --green:#2a9a1e;
  --red:#d01d1d;
  --navy:#1e2c5a;
}
*{box-sizing:border-box;margin:0;padding:0}
html,body{width:1070px;height:1200px;overflow:hidden}
body{position:relative;font-family:"Arimo",Arial,sans-serif;background:#fff;color:var(--text)}
.abs{position:absolute}
.header{left:0;top:0;width:1070px;height:78px;background:linear-gradient(90deg,#fff 60%,#ececec)}
.brand{left:178px;top:40px;font-size:13px;font-weight:700;color:var(--brown-dark);letter-spacing:.5px}
.brand-mark{left:178px;top:14px;width:20px;height:20px;background:var(--orange)}
.apply{left:778px;top:32px;width:115px;height:32px;background:var(--orange);border:2px solid #f9a566;color:#fff;font-size:12px;display:flex;align-items:center;justify-content:center;gap:6px}
.nav{left:0;top:78px;width:1070px;height:32px;background:var(--brown);border-bottom:3px solid var(--brown-dark)}
.nav ul{position:absolute;left:178px;top:0;display:flex;list-style:none;height:29px}
.nav li{padding:0 15px;font-size:11.5px;color:#d9c9bb;line-height:29px;border-right:1px solid #6b4527}
.nav li.active{background:var(--orange);color:#fff}
.ticker{left:178px;top:112px;width:715px;height:27px;background:#f4f4f4;display:flex;justify-content:space-around;align-items:center;font-size:8.5px;color:var(--navy)}
.ticker .up{color:var(--green)}.ticker .down{color:var(--red)}
.ticker-band{left:0;top:112px;width:1070px;height:27px;background:#ececec}
.stage{left:0;top:139px;width:1070px;height:296px;background:linear-gradient(90deg,#e4e4e4,#f2f2f2 50%,#e4e4e4)}
.slide{left:178px;top:152px;width:715px;height:281px;background:linear-gradient(120deg,#d6d8dc,#f2f2f2 45%,#9ea3aa)}
.caption{left:178px;top:347px;width:715px;height:86px;background:rgba(20,20,20,.82);padding:6px 19px;color:#fff}
.caption h2{font-size:35px;font-weight:400;letter-spacing:-.5px;line-height:38px}
.caption p{font-size:12.5px;line-height:18px;color:#ddd;letter-spacing:-.3px}
.welcome{left:0;top:435px;width:1070px;height:186px;background:#fff;border-bottom:1px solid #ddd}
.welcome h1{position:absolute;left:178px;top:15px;font-size:22px;color:var(--brown);letter-spacing:-.2px}
.welcome p{position:absolute;left:178px;top:48px;width:515px;font-size:8.3px;line-height:14.2px}
.btn{background:var(--brown);color:#fff;font-size:10px;height:24px;line-height:22px;padding:0 7px;border:1px solid var(--brown-dark);box-shadow:0 0 0 1px #c9a98c inset;display:inline-block}
.access{left:711px;top:454px;width:182px;height:149px;background:var(--orange)}
.access h3{background:var(--brown);color:#fff;font-size:18px;height:28px;line-height:28px;padding-left:14px}
.field{margin:4px 8px 0;height:25px;background:#fff;border:1px solid #f8b680;font-size:9px;color:#999;line-height:23px;padding-left:6px}
.remember{margin:6px 9px 0;display:flex;align-items:center;gap:5px;color:#fff;font-size:7.5px}
.remember span.box{width:12px;height:12px;background:#eee;display:flex;align-items:center;justify-content:center}
.login{margin:5px 0 0 28px;background:var(--brown);color:#fff;font-size:11px;width:124px;height:24px;line-height:24px;text-align:center;box-shadow:0 0 0 1px #c9a98c inset}
.features{left:0;top:621px;width:1070px;height:189px;background:linear-gradient(90deg,#dcdcdc,#f5f5f5 25%,#f5f5f5 75%,#dcdcdc)}
.feature{top:15px;width:242px;text-align:center}
.feature h4{font-size:15.5px;color:var(--brown);font-weight:400;margin:12px 0 8px}
.feature p{font-size:8.3px;line-height:12px;padding:0 10px}
.feature .btn{margin-top:17px}
.verified{left:0;top:810px;width:1070px;height:82px;background:linear-gradient(#fff,#ececec)}
.verified .title{position:absolute;top:12px;width:1070px;text-align:center;font-size:12px;color:#555}
.badge{position:absolute;top:42px;height:34px}
.footer{left:0;top:910px;width:1070px;height:176px;background:var(--footer)}
.fcol{top:18px;padding-right:14px;border-right:1px dotted #777;height:148px}
.fcol.last{border-right:none}
.fcol h5{color:var(--orange);font-size:11px;margin-bottom:6px}
.fcol a{display:block;color:#aaa;font-size:8.3px;line-height:15.7px;text-decoration:none}
.disclaimer{left:0;top:1086px;width:1070px;height:82px;background:var(--footer-2);padding:9px 178px 0;font-size:7.8px;line-height:11.5px;color:#888}
.disclaimer p+p{margin-top:6px}
.bottom{left:0;top:1168px;width:1070px;height:32px;background:var(--footer-3);font-size:8px;color:#777}
</style>
</head>
<body>
<header class="abs header">
  <div class="abs brand-mark"></div>
  <div class="abs brand">MARLOWE CAPITAL GROUP</div>
  <div class="abs apply">
    <svg width="16" height="14" viewBox="0 0 16 14"><rect x="1" y="1" width="14" height="9" fill="none" stroke="#fff" stroke-width="1.4"/><path d="M4 4h8M4 7h5M4 10l-1 3 4-3" stroke="#fff" stroke-width="1.4" fill="none"/></svg>
    APPLY NOW
  </div>
</header>
<nav class="abs nav">
  <ul>
    <li class="active">HOME</li><li>ABOUT US</li><li>INVESTMENTS</li><li>FUNDS</li><li>BROKERAGE</li><li>EXCHANGE</li><li>ACCOUNTS</li><li style="border:none">CONTACT US</li>
  </ul>
</nav>
<div class="abs ticker-band"></div>
<div class="abs ticker">
  <span>AH= <span class="up">12.65761▲</span></span>
  <span>GBP/UGX= <span class="down">4010.061274▼</span></span>
  <span>GBP/UAH= <span class="up">12.65761▲</span></span>
  <span>GBP/UAH= <span class="up">12.65761▲</span></span>
  <span>GBP/UAH= <span class="up">12.65761▲</span></span>
  <span>GBP/UAH= <span class="up">12.65761▲</span></span>
</div>
<section class="abs stage">
  <svg class="abs" style="left:144px;top:120px" width="22" height="66" viewBox="0 0 22 66"><path d="M20 1L2 33l18 32" fill="none" stroke="#888" stroke-width="1.5"/></svg>
  <svg class="abs" style="left:905px;top:120px" width="22" height="66" viewBox="0 0 22 66"><path d="M2 1l18 32L2 65" fill="none" stroke="#888" stroke-width="1.5"/></svg>
</section>
<div class="abs slide" role="img" aria-label="Photo of a team of advisers meeting in an office in front of a whiteboard with charts"></div>
<div class="abs caption">
  <h2>TEAMWORK FOR YOUR BENEFIT</h2>
  <p>Our Dedicated Private Bankers, Will Proactively Keep You Up To Date With Relevent Information And Provide A Financial Overview That Enables You To Make Better Decisions.</p>
</div>
<section class="abs welcome">
  <h1>WELCOME TO MARLOWE CAPITAL GROUP</h1>
  <p>Lorem ipsum dolor sit amet, consectetur adipiscing elit. Nulla a vulputate diam. Class aptent taciti sociosqu ad litora torquent per conubia nostra, per inceptos himenaeos. Pellentesque vel nisi diam. Mauris nisl tellus, scelerisque quis felis quis, convallis congue lacus. Vivamus egestas mauris non purus interdum tempus. Praesent tincidunt arcu id ultricies ultricies. Pellentesque ultrices ipsum vel accumsan rhoncus. Suspendisse pharetra turpis eget tempor laoreet. Vestibulum mattis non sapien a rhoncus. Vivamus consectetur nulla enim, et interdum massa vestibulum quis.</p>
  <span class="btn abs" style="left:178px;top:143px">Read More</span>
</section>
<aside class="abs access">
  <h3>PRIVATE ACCESS</h3>
  <div class="field" style="margin-top:6px">ACC. Number</div>
  <div class="field">ACC. Password</div>
  <div class="remember"><span class="box"><svg width="9" height="8" viewBox="0 0 9 8"><path d="M1 4l2.5 2.5L8 1" stroke="#555" stroke-width="1.6" fill="none"/></svg></span>Forgot ACC Number/Password?</div>
  <div class="login">Log In To Accounts</div>
</aside>
<section class="abs features">
  <div class="abs feature" style="left:172px">
    <svg width="30" height="32" viewBox="0 0 30 32"><circle cx="15" cy="8" r="7" fill="var(--orange)"/><path d="M1 31c0-9 6-14 14-14s14 5 14 14z" fill="var(--orange)"/><path d="M15 18l-2 6 2 4 2-4z" fill="#fff"/></svg>
    <h4>MANAGEMENT &amp; STRATEGY</h4>
    <p>Lorem ipsum dolor sit amet, conectetur adipiscing elit. Etiam semper leo quis rutrum ferentum. Donec nulla sem, laoret non justo at, volutat pulvinar felis. Etiam convallis turpis cursus tortor pellentesque.</p>
    <span class="btn">Read More</span>
  </div>
  <div class="abs feature" style="left:414px">
    <svg width="32" height="32" viewBox="0 0 32 32"><rect x="1" y="2" width="30" height="14" rx="1" fill="none" stroke="var(--orange)" stroke-width="2"/><circle cx="16" cy="9" r="4" fill="var(--orange)"/><circle cx="8" cy="22" r="4" fill="var(--orange)"/><circle cx="23" cy="22" r="4" fill="var(--orange)"/><circle cx="16" cy="28" r="4" fill="var(--orange)"/></svg>
    <h4>FUNDS</h4>
    <p>Lorem ipsum dolor sit amet, conectetur adipiscing elit. Etiam semper leo quis rutrum ferentum. Donec nulla sem, laoret non justo at, volutat pulvinar felis. Etiam convallis turpis cursus tortor pellentesque.</p>
    <span class="btn">Read More</span>
  </div>
  <div class="abs feature" style="left:657px">
    <svg width="32" height="32" viewBox="0 0 32 32"><circle cx="11" cy="12" r="10" fill="var(--orange)"/><circle cx="21" cy="20" r="10" fill="var(--orange-dark)" stroke="#f5f5f5" stroke-width="2"/><path d="M24 16a4 4 0 1 0 0 8M17 19h5M17 21.5h5" stroke="#fff" stroke-width="1.6" fill="none"/></svg>
    <h4>CURRENCY EXCHANGE</h4>
    <p>Lorem ipsum dolor sit amet, conectetur adipiscing elit. Etiam semper leo quis rutrum ferentum. Donec nulla sem, laoret non justo at, volutat pulvinar felis. Etiam convallis turpis cursus tortor pellentesque.</p>
    <span class="btn">Read More</span>
  </div>
</section>
<section class="abs verified">
  <div class="title">Verified and Protected By</div>
  <div class="badge" style="left:298px;width:78px;border-radius:17px;background:#e8d6da" role="img" aria-label="Security certificate badge"></div>
  <div class="badge" style="left:432px;width:102px;background:#dbeed6" role="img" aria-label="Privacy certificate badge"></div>
  <div class="badge" style="left:598px;width:34px;border-radius:50%;background:#2b3f86" role="img" aria-label="Assurance seal badge"></div>
  <div class="badge" style="left:698px;width:68px;top:46px;height:26px;background:#2a5aa8" role="img" aria-label="Auditor badge"></div>
</section>
<div class="abs" style="left:0;top:892px;width:1070px;height:18px;background:#e2e2e2"></div>
<footer class="abs footer">
  <div class="abs fcol" style="left:178px"><h5>ABOUT US</h5><a>Hisory</a><a>Expertize</a><a>Identity</a><a>Stragedy</a><a>Contact Us</a></div>
  <div class="abs fcol" style="left:267px"><h5>INVESTMENT</h5><a>Term Deposits</a><a>Management &amp; Strategy</a><a>Client Relations</a><a>Financial Privacy</a><a>Tax Advice</a><a>Wealth Analysis &amp; Financial Planning</a><a>Active Advissory Group</a><a>Manager Selection Services</a></div>
  <div class="abs fcol" style="left:445px"><h5>FUNDS</h5><a>Overview</a><a>Administration</a><a>Funds Security</a><a>Core Services</a><a>Reporting</a><a>Revenue Opportunities</a><a>How it works?</a><a>Glossary</a></div>
  <div class="abs fcol" style="left:568px"><h5>CURRENCY EXCHANGE</h5><a>Foreign Exchange</a><a>Fx Forward</a><a>Fx Options</a></div>
  <div class="abs fcol" style="left:727px"><h5>ACCOUNTS</h5><a>Apply Now</a><a>Private Access</a></div>
  <div class="abs fcol last" style="left:822px"><h5>BROKERAGE</h5><a>Institutional</a><a>Research</a><a>Trading</a></div>
</footer>
<div class="abs disclaimer">
  <p>Lorem ipsum dolor sit amet, consectetur adipiscing elit. Etiam semper leo quis rutrum fermentum. Donec nulla sem, laoreet non justo at, volutpat pulvinar felis. Etiam convallis turpis cursus tortor pellentesque aliquam. Quisque in adipiscing purus. Nunc feugiat pulvinar feugiat. Integer nibh dolor, convallis nec sodales ut, adipiscing sed tellus. Vestibulum non orci turpis. Pellentesque ullamcorper turpis in elit viverra, at egestas ipsum lacinia.</p>
  <p>Proin dignissim enim non nulla aliquet, ac placerat lorem aliquet. Aliquam consequat, metus a lacinia fermentum, dolor magna semper leo, volutpat dictum diam nunc sed sem. Pellentesque habitant morbi tristique senectus et netus et malesuada fames ac turpis egestas. Aliquam blandit orci ante, nec ornare metus faucibus sed. Sed iaculis.</p>
</div>
<div class="abs bottom">
  <span class="abs" style="left:178px;top:11px">© 2009-2013 MarloweCapitalGroup. All rights reserved.</span>
  <span class="abs" style="left:826px;top:11px">Legal Disclaimer</span>
</div>
</body>
</html>
```